Ashmoor "Past Cold Embers" Single Album Artwork

Ashmoor is a hard rock / metal band that are releasing two singles and a full album. The two singles and album will have each their own album cover artwork. Of course as any rock or metal band we like a more rock n roll look when it comes to graphic arts.

Past cold embers is a song that we need an album cover for and we have a faint idea of what could be the cover but we have no idea how hard it could be to make. Essentially we want the cover to be us 4 band members standing on a cliff under a glazing sun. The issue we have is we don't have a photo of us standing on a cliff, instead we have a photo of us four together on sand (see below) Unsure if this design is possible we hope that one designer is talented enough to be able to complete our request. Otherwise as always, any entrepreneurial designers can send in a design they think may be better.

The band is a rock / metal band so it has to look like a rock / metal band cover - just keep that in mind.

```html
<!DOCTYPE html>
<html lang="en">
<head>
<meta charset="utf-8">
<title>Ashmoor – Past Cold Embers</title>
<link rel="stylesheet" href="https://fonts.googleapis.com/css2?family=Rye&family=Great+Vibes&display=swap">
<style>
  :root {
    --orange: #f29100;
    --black: #000000;
    --white: #ffffff;
    --title-gold: #f6a12b;
    --halo-tan: #a08a64;
    --photo-dark: #2d3a22;
    --photo-mid: #6b6a4a;
    --photo-light: #b9a98a;
  }
  * { margin: 0; padding: 0; box-sizing: border-box; }
  html, body { width: 1197px; height: 1200px; overflow: hidden; background: var(--orange); }
  .cover { position: relative; width: 1197px; height: 1200px; overflow: hidden; background: var(--orange); }
  .cover-art { position: absolute; inset: 0; }
  .band-name {
    position: absolute; left: 0; right: 0; top: 150px;
    text-align: center;
    font-family: "Rye", serif;
    font-weight: 400;
    font-size: 148px; line-height: 1;
    color: var(--white);
    letter-spacing: 2px;
  }
  .single-title {
    position: absolute; left: 0; right: 0; top: 420px;
    text-align: center;
    font-family: "Great Vibes", cursive;
    font-weight: 400;
    font-size: 180px; line-height: 160px;
    color: var(--title-gold);
  }
</style>
</head>
<body>
<main class="cover">
  <svg class="cover-art" width="1197" height="1200" viewBox="0 0 1197 1200">
    <defs>
      <linearGradient id="band-photo-tone" x1="0" y1="0" x2="0" y2="1">
        <stop offset="0" stop-color="var(--photo-dark)"/>
        <stop offset="0.55" stop-color="var(--photo-mid)"/>
        <stop offset="1" stop-color="var(--photo-light)"/>
      </linearGradient>
      <radialGradient id="sun-glow" cx="604" cy="616" r="420" gradientUnits="userSpaceOnUse">
        <stop offset="0" stop-color="#ffffff"/>
        <stop offset="0.35" stop-color="#9a9a9a"/>
        <stop offset="0.75" stop-color="#1c1c1c"/>
        <stop offset="1" stop-color="#000000" stop-opacity="0"/>
      </radialGradient>
      <radialGradient id="halo-tone" cx="612" cy="650" r="370" gradientUnits="userSpaceOnUse">
        <stop offset="0.7" stop-color="var(--halo-tan)" stop-opacity="0"/>
        <stop offset="0.86" stop-color="var(--halo-tan)" stop-opacity="0.55"/>
        <stop offset="1" stop-color="var(--halo-tan)" stop-opacity="0"/>
      </radialGradient>
    </defs>

    <g class="band-photo" role="img" aria-label="Photo of the four band members standing in front of dry brush">
      <path d="M182 300 V100 A99 99 0 0 1 380 100 A99 99 0 0 1 579 100 A99 99 0 0 1 777 100 A99 99 0 0 1 976 100 V300 Z" fill="url(#band-photo-tone)"/>
    </g>

    <circle class="record-disc" cx="603" cy="722" r="537" fill="var(--black)"/>
    <circle class="sun-glow" cx="604" cy="616" r="420" fill="url(#sun-glow)"/>
    <circle class="sun-halo" cx="612" cy="650" r="370" fill="url(#halo-tone)" role="img" aria-label="Tangled ring ornament around the sun"/>
  </svg>

  <h1 class="band-name">Ashmoor</h1>
  <h2 class="single-title">Past cold<br>embers</h2>
</main>
</body>
</html>
```